Dietitian needs awesome business card

I need a contemporary design that's eye catching but professional.
My card is to given to doctors, specialists and patients alike.
I manage patients with chronic diseases
I have uploaded my logo and current business card, I would also like the other Registered Clinical Nutritionist logo incorporated into the design

Target Market(s)

Doctors, specialists and patients

Industry/Entity Type

Healthcare

Contact Information for Business Card

www.brindlecovenutrition.com.au
Ph: 0427 516 903
Fax: 6482 7315
email: marcus.k.wellfare@quorvamail.com
Space on the back of the card with: Appointment date, Appointment time and appointment location

Font styles to use
Serif

Colors
fbee3e
876aae
ffc214

Requirements
Must have
• My Logo
• Registered Clinical Nutritionist Logo
• My 4 locations - Fernhollow Medical Centre, North Kelby Health, Ashcourt Medical, Pinebrook Doctors Surgery
Nice to have
• I like the colours in my current business card

```html
<!DOCTYPE html>
<html lang="en">
<head>
<meta charset="utf-8">
<title>Brindlecove Nutrition &amp; Dietetics – Business Card</title>
<link href="https://fonts.googleapis.com/css2?family=Questrial&family=Lora:ital@1&display=swap" rel="stylesheet">
<style>
  :root {
    --bg: #3b3b3b;
    --card-white: #ffffff;
    --card-grey: #ececec;
    --green: #8cc63f;
    --green-soft: #b8d88a;
    --green-quote: #c9dfa6;
    --quote-text: #5f6f4a;
    --blue: #1f3c8e;
    --orange: #ef7622;
    --ink: #1b1b1b;
    --label: #2a2a2a;
  }
  * { box-sizing: border-box; margin: 0; padding: 0; }
  html, body { width: 1200px; height: 1048px; overflow: hidden; }
  body {
    background: var(--bg);
    font-family: "Questrial", sans-serif;
    position: relative;
  }
  .card {
    position: absolute;
    left: 190px;
    width: 820px;
    height: 470px;
    border-radius: 22px;
    overflow: hidden;
    box-shadow: 0 10px 30px rgba(0,0,0,.45);
  }

  /* ---------- Appointment side ---------- */
  .card--appointment { top: 36px; background: var(--card-white); }
  .appt-band-left {
    position: absolute; left: 0; top: 26px; width: 170px; height: 54px;
    background: var(--green);
  }
  .appt-band-right {
    position: absolute; right: 0; top: 90px; width: 410px; height: 118px;
    background: var(--green);
  }
  .appt-quote {
    position: absolute; right: 78px; top: 90px; width: 140px; height: 118px;
    background: var(--green-quote);
    font-family: "Lora", serif; font-style: italic;
    font-size: 15px; line-height: 17px; color: var(--quote-text);
    display: flex; align-items: center; justify-content: center; text-align: center;
    padding: 8px;
  }
  .brand {
    position: absolute; display: flex; align-items: center; gap: 12px;
  }
  .brand-dot {
    border-radius: 50%; background: var(--green); flex: none;
  }
  .brand-name {
    color: var(--blue); font-weight: 400; line-height: 1;
  }
  .card--appointment .brand { left: 156px; top: 24px; }
  .card--appointment .brand-dot { width: 60px; height: 60px; border: 4px solid var(--card-white); }
  .card--appointment .brand-name { font-size: 34px; }
  .card--appointment .brand-sub { font-size: 17px; display: block; margin-top: 4px; }

  .appt-title {
    position: absolute; left: 420px; top: 232px;
    font-size: 30px; color: var(--green-soft); letter-spacing: .5px; font-weight: 400;
  }
  .appt-row {
    position: absolute; left: 400px; right: 0;
    border-bottom: 2px solid var(--green);
    font-size: 20px; color: var(--label);
    height: 42px; display: flex; align-items: flex-end; padding-bottom: 4px;
  }
  .appt-row--name { top: 262px; }
  .appt-row--date { top: 304px; }
  .appt-row--location { top: 346px; }
  .appt-row--blank { top: 394px; }
  .appt-time { margin-left: 200px; }

  /* ---------- Contact side ---------- */
  .card--contact {
    top: 542px;
    background: linear-gradient(120deg, var(--card-grey) 0%, #f6f6f6 55%, #e9e9e9 100%);
  }
  .credential-badge {
    position: absolute; left: 38px; top: 30px; width: 130px; height: 50px;
    background: var(--orange); border-radius: 2px;
  }
  .card--contact .brand { left: 52px; top: 200px; }
  .card--contact .brand-dot { width: 74px; height: 74px; }
  .card--contact .brand-name { font-size: 42px; }
  .card--contact .brand-sub { font-size: 21px; display: block; margin-top: 6px; }

  .divider {
    position: absolute; left: 430px; top: 70px; bottom: 0;
    width: 2px; background: var(--green);
  }
  .person-name {
    position: absolute; top: 106px; left: 0; width: 100%; height: 40px;
    font-size: 30px; color: var(--green); font-weight: 400; white-space: nowrap;
  }
  .person-first {
    position: absolute; right: 398px; top: 0;
    font-weight: 700; -webkit-text-stroke: .7px var(--green);
  }
  .person-last { position: absolute; left: 440px; top: 0; }
  .person-role {
    position: absolute; left: 440px; top: 146px;
    font-size: 21px; line-height: 26px; color: var(--green);
  }
  .contact-list {
    position: absolute; left: 442px; top: 282px; list-style: none;
  }
  .contact-list li {
    display: flex; align-items: center; gap: 14px;
    font-size: 20px; color: var(--ink); height: 34px; white-space: nowrap;
  }
  .contact-list svg { width: 20px; height: 20px; flex: none; }
  .icon { fill: var(--green); stroke: none; }
  .icon-line { fill: none; stroke: var(--green); stroke-width: 1.6; }
</style>
</head>
<body>

  <section class="card card--appointment" aria-label="Card back: appointment details">
    <div class="appt-band-left"></div>
    <div class="appt-band-right"></div>
    <div class="appt-quote">“Let food be thy medicine and medicine be thy food”</div>

    <div class="brand">
      <span class="brand-dot"></span>
      <span class="brand-name">Brindlecove<span class="brand-sub">Nutrition &amp; Dietetics</span></span>
    </div>

    <h2 class="appt-title">Appointment</h2>
    <div class="appt-row appt-row--name">Name</div>
    <div class="appt-row appt-row--date">Date</div>
    <div class="appt-row appt-row--location">Location<span class="appt-time">Time</span></div>
    <div class="appt-row appt-row--blank"></div>
  </section>

  <section class="card card--contact" aria-label="Card front: contact details">
    <div class="credential-badge" role="img" aria-label="Credential badge"></div>

    <div class="brand">
      <span class="brand-dot"></span>
      <span class="brand-name">Brindlecove<span class="brand-sub">Nutrition &amp; Dietetics</span></span>
    </div>

    <div class="divider"></div>

    <h1 class="person-name"><span class="person-first">Marcus</span> <span class="person-last">Kellaway</span></h1>
    <p class="person-role">Registered Clinical Nutritionist<br>Nutritionist and Chef</p>

    <ul class="contact-list">
      <li>
        <svg viewBox="0 0 20 20" aria-hidden="true"><path class="icon" d="M2 7c0-2 3-4 8-4s8 2 8 4v2h-4V7H6v2H2z"/><rect class="icon" x="4" y="10" width="12" height="7" rx="1.5"/></svg>
        0427 516 903
      </li>
      <li>
        <svg viewBox="0 0 20 20" aria-hidden="true"><rect class="icon-line" x="2" y="4.5" width="16" height="11"/><path class="icon-line" d="M2 4.5l8 6 8-6"/></svg>
        marcus.k.wellfare@quorvamail.com
      </li>
      <li>
        <svg viewBox="0 0 20 20" aria-hidden="true"><rect class="icon" x="5" y="2" width="10" height="6"/><rect class="icon" x="2" y="8" width="16" height="8" rx="1.5"/></svg>
        6482 7315
      </li>
      <li>
        <svg viewBox="0 0 20 20" aria-hidden="true"><circle class="icon-line" cx="10" cy="10" r="8"/><ellipse class="icon-line" cx="10" cy="10" rx="3.5" ry="8"/><path class="icon-line" d="M2 10h16M3.5 6h13M3.5 14h13"/></svg>
        www.brindlecovenutrition.com.au
      </li>
    </ul>
  </section>

</body>
</html>
```